Natural Supplement Co Needs Label Makeover

Our company's success began with our main product, an amino acid blend that aids in fat metabolism, called Vantorel. Since then we continue to expand the product line that now includes a detox called Vantopure, and probiotic called Vantoflora, as well as 3 others, for a total of 6 products/ labels.
Our original design/logo had more of an 'old-timey' feel (see attached 2-product photo). We are looking for a fresh label design update for the product line which reflects the range of supplements as cohesive and individual parts of an overall health plan/strategy (see attached 'Logo Update Test' as just one idea we had in-house, you need not consider it as a starting point).

Target Market(s)

women 25-45

Industry/Entity Type

Health And Wellness

Requirements
Must have
• consistent theme with confident look
Nice to have
• Each product (ie. "Vantorel") has a few-word descriptor: ("Fat-Burning Amino Acids") that should be planned on including as part of each label.
Should not have
• NO 'streamlined' or graphic interpretations of the human body, or figurative image

```html
<!DOCTYPE html>
<html lang="en">
<head>
<meta charset="utf-8">
<title>Vantopure and Vantocore labels</title>
<link href="https://fonts.googleapis.com/css2?family=Jost:wght@300;400&display=swap" rel="stylesheet">
<style>
  :root {
    --page-bg: #efefef;
    --paper: #ffffff;
    --blue-deep: #1f5f98;
    --blue-mid: #3d86c0;
    --blue-light: #a8cdea;
    --blue-ink: #2a6aa6;
    --gold-deep: #b88a14;
    --gold-mid: #dcac2a;
    --gold-light: #f6dc86;
    --gold-ink: #d19f1e;
    --body-ink: #2a3a55;
  }
  * { margin: 0; padding: 0; box-sizing: border-box; }
  html, body {
    width: 1200px; height: 866px; overflow: hidden;
    background: var(--page-bg);
    font-family: "Jost", "Futura", sans-serif;
  }
  .canvas { position: relative; width: 1200px; height: 866px; }

  .label {
    position: absolute; top: 200px;
    width: 300px; height: 460px; overflow: hidden;
  }
  .label--pure { left: 170px; background: linear-gradient(90deg, var(--blue-deep) 0%, var(--blue-mid) 55%, var(--blue-light) 100%); --ink: var(--blue-ink); }
  .label--core { left: 730px; background: linear-gradient(90deg, var(--gold-deep) 0%, var(--gold-mid) 55%, var(--gold-light) 100%); --ink: var(--gold-ink); }

  .label__panel { position: absolute; inset: 0; width: 300px; height: 460px; }

  .label__initials {
    position: absolute; left: 28px; top: 56px;
    font-weight: 300; font-size: 66px; line-height: 1; color: var(--paper);
  }
  .label__initials--small { top: 84px; font-size: 38px; }

  .label__name {
    position: absolute; left: 36px; top: 200px;
    font-weight: 300; font-size: 30px; line-height: 1; color: var(--ink);
    letter-spacing: 0.5px; text-transform: uppercase;
  }
  .label__name sup { font-size: 8px; vertical-align: top; margin-left: 1px; }

  .label__descriptor {
    position: absolute; left: 36px; top: 236px; width: 204px;
    font-weight: 300; font-size: 15.5px; line-height: 1.2; color: var(--ink);
    padding-bottom: 3px; border-bottom: 1.5px solid var(--ink);
    white-space: nowrap;
  }

  .label__copy {
    position: absolute; left: 42px; top: 274px; width: 194px;
    font-size: 6.5px; line-height: 1.5; color: var(--body-ink);
    text-align: justify; text-align-last: center;
  }

  .label__volume {
    position: absolute; left: 0; right: 0; bottom: 8px;
    text-align: center; font-size: 14px; font-weight: 400; line-height: 1; color: var(--paper);
  }
  .label__arc-text { font-family: "Jost", sans-serif; font-size: 6px; fill: var(--body-ink); }
</style>
</head>
<body>
<main class="canvas">

  <section class="label label--pure">
    <svg class="label__panel" viewBox="0 0 300 460" aria-hidden="true">
      <path id="pure-arc" d="M116 418 C188 418 256 372 274 300" fill="none"/>
      <path d="M30 146 H172 C240 146 286 206 286 286 C286 372 222 428 148 428 C80 428 30 384 30 326 Z" fill="var(--paper)"/>
      <text class="label__arc-text"><textPath href="#pure-arc">Shake well before use and store in a cool dry place</textPath></text>
    </svg>
    <div class="label__initials">VP</div>
    <h2 class="label__name">Vantopure<sup>TM</sup></h2>
    <p class="label__descriptor">Fat-Burning Amino Acids</p>
    <p class="label__copy">A daily blend of amino acids made to support natural fat metabolism, steady energy and a balanced routine. Take one dropper each morning with water or juice. Best used as part of a full plan of whole foods, rest and regular movement every week.</p>
    <p class="label__volume">25 ML</p>
  </section>

  <section class="label label--core">
    <svg class="label__panel" viewBox="0 0 300 460" aria-hidden="true">
      <path id="core-arc" d="M116 418 C188 418 256 372 274 300" fill="none"/>
      <path d="M30 146 H172 C240 146 286 206 286 286 C286 372 222 428 148 428 C80 428 30 384 30 326 Z" fill="var(--paper)"/>
      <text class="label__arc-text"><textPath href="#core-arc">Shake well before use and store in a cool dry place</textPath></text>
    </svg>
    <div class="label__initials label__initials--small">VC</div>
    <h2 class="label__name">Vantocore<sup>TM</sup></h2>
    <p class="label__descriptor">Fat-Burning Amino Acids</p>
    <p class="label__copy">A daily blend of amino acids made to support natural fat metabolism, steady energy and a balanced routine. Take one dropper each morning with water or juice. Best used as part of a full plan of whole foods, rest and regular movement every week.</p>
    <p class="label__volume">25 ML</p>
  </section>

</main>
</body>
</html>
```